Steady-Point Snack Vending Needs a Promotional Flyer

Design a one page, one sided 8 1/2" x 11" flyer that can be handed out to potential customers. Please keep printing efficiencies in mind. See attached old flyers and company website (steadypointvend.com) for reference of services. I have also attached our current logo.

```html
<!DOCTYPE html>
<html lang="en">
<head>
<meta charset="utf-8">
<title>Steady-Point Snack Vending – Flyer</title>
<link href="https://fonts.googleapis.com/css2?family=League+Spartan:wght@600;700;800&family=Montserrat:wght@500;600&display=swap" rel="stylesheet">
<style>
  :root{
    --navy:#14293a;
    --navy-deep:#0e1d29;
    --sky:#3fa9e0;
    --sky-light:#6fc0e8;
    --white:#ffffff;
    --paper:#ffffff;
  }
  *{margin:0;padding:0;box-sizing:border-box}
  html,body{width:939px;height:1200px;overflow:hidden;background:var(--paper)}
  .flyer{position:relative;width:939px;height:1200px;overflow:hidden;background:var(--paper);font-family:"Montserrat",sans-serif;color:var(--navy)}
  .diagonal{position:absolute;left:0;top:0}
  .brand{position:absolute;left:55px;top:112px;display:flex;align-items:center;gap:14px}
  .brand-mark{width:40px;height:40px;background:var(--sky)}
  .brand-name{font-family:"League Spartan",sans-serif;font-weight:800;font-size:30px;line-height:1.05;color:var(--navy);width:300px}
  .call{position:absolute;left:597px;top:72px;width:287px;text-align:center}
  .call-label{font-family:"League Spartan",sans-serif;font-weight:600;font-size:20px;color:var(--white);letter-spacing:.5px;margin-left:40px}
  .call-pill{margin-top:10px;height:52px;background:var(--navy);border-radius:6px;display:flex;align-items:center;justify-content:center;gap:12px}
  .call-pill svg{width:34px;height:34px}
  .call-number{font-family:"League Spartan",sans-serif;font-weight:700;font-size:33px;color:var(--white);padding-top:4px}
  .accent-bar{position:absolute;left:0;top:345px;width:11px;height:215px;background:var(--sky)}
  .headline{position:absolute;left:55px;top:352px;font-family:"League Spartan",sans-serif;color:var(--navy)}
  .headline .pre{font-weight:700;font-size:30px}
  .headline .big{font-weight:800;font-size:78px;line-height:.95;margin-top:14px}
  .headline .post{font-weight:700;font-size:27px;margin-top:10px}
  .machine{position:absolute}
  .machine-snack{left:439px;top:209px;width:314px;height:567px;background:linear-gradient(180deg,#2b2f33,#17191b)}
  .machine-drink{left:774px;top:200px;width:165px;height:576px;background:linear-gradient(180deg,#c8242b,#8e1a1f)}
  .services-band{position:absolute;left:0;top:712px;width:939px;height:424px;background:var(--navy)}
  .services{position:absolute;left:55px;top:820px;width:829px;height:105px;display:flex;border-left:1px solid #3b5365}
  .service{flex:1;border-right:1px solid #3b5365;text-align:center}
  .service svg{width:54px;height:54px;display:block;margin:0 auto}
  .service-name{margin-top:28px;font-family:"League Spartan",sans-serif;font-weight:700;font-size:21px;color:var(--white)}
  .values{position:absolute;left:55px;top:966px;display:grid;grid-template-columns:430px 400px;row-gap:13px;list-style:none}
  .values li{display:flex;align-items:center;gap:10px;font-size:15px;font-weight:500;color:var(--white);height:19px}
  .values svg{width:16px;height:16px;flex:none}
  .footer{position:absolute;left:0;top:1136px;width:939px;height:64px;background:var(--sky)}
  .footer-web{position:absolute;left:0;top:0;height:64px}
  .footer-web-text{position:absolute;left:55px;top:20px;font-family:"League Spartan",sans-serif;font-weight:700;font-size:21px;color:var(--white)}
  .footer-address{position:absolute;left:397px;top:22px;font-family:"Montserrat",sans-serif;font-weight:600;font-size:16px;color:var(--white)}
</style>
</head>
<body>
<div class="flyer">
  <svg class="diagonal" width="939" height="712" viewBox="0 0 939 712" aria-hidden="true">
    <defs>
      <linearGradient id="bandFade" x1="0" y1="0" x2="1" y2="1">
        <stop offset="0" stop-color="#4aa9d8"/>
        <stop offset="1" stop-color="#3b8fbd"/>
      </linearGradient>
    </defs>
    <polygon points="704,0 939,0 939,712 282,712" fill="url(#bandFade)"/>
    <polygon points="704,0 800,0 440,712 282,712" fill="#6fb9de" opacity=".45"/>
  </svg>

  <div class="brand">
    <div class="brand-mark"></div>
    <div class="brand-name">Steady-Point Snack Vending</div>
  </div>

  <div class="call">
    <div class="call-label">CALL US AT</div>
    <div class="call-pill">
      <svg viewBox="0 0 34 34" aria-hidden="true"><circle cx="17" cy="17" r="17" fill="var(--sky)"/><path d="M12 9c1 0 2 3 2.5 4s-1.5 2-1 3 3 4 4.5 4.5 2-1 3-1 4 1.5 4 2.5-1.5 3-3 3C17 25 9 17 9 12c0-1.5 2-3 3-3z" fill="#fff"/></svg>
      <span class="call-number">630-555-0147</span>
    </div>
  </div>

  <div class="accent-bar"></div>
  <div class="headline">
    <div class="pre">One of Chicagoland's</div>
    <div class="big">Premier<br>Vending</div>
    <div class="post">Companies</div>
  </div>

  <div class="machine machine-drink" role="img" aria-label="Photo of a red drinks vending machine stocked with bottled beverages"></div>
  <div class="machine machine-snack" role="img" aria-label="Photo of a black snack vending machine stocked with chips and candy"></div>

  <div class="services-band"></div>
  <div class="services">
    <div class="service">
      <svg viewBox="0 0 54 54" fill="none" stroke="var(--sky)" stroke-width="2.5"><rect x="11" y="4" width="32" height="46" rx="2"/><rect x="15" y="9" width="18" height="28"/><line x1="15" y1="16" x2="33" y2="16"/><line x1="15" y1="23" x2="33" y2="23"/><line x1="15" y1="30" x2="33" y2="30"/><line x1="37" y1="11" x2="40" y2="11"/><line x1="37" y1="17" x2="40" y2="17"/><rect x="15" y="41" width="24" height="5"/></svg>
      <div class="service-name">VENDING</div>
    </div>
    <div class="service">
      <svg viewBox="0 0 54 54" fill="none" stroke="var(--sky)" stroke-width="2.5"><path d="M10 24h28v6c0 8-6 14-14 14s-14-6-14-14z"/><path d="M38 28h4a5 5 0 0 1 0 10h-6"/><line x1="4" y1="48" x2="46" y2="48"/><path d="M18 6c-3 4 3 6 0 12M24 6c-3 4 3 6 0 12M30 6c-3 4 3 6 0 12"/></svg>
      <div class="service-name">COFFEE SERVICE</div>
    </div>
    <div class="service">
      <svg viewBox="0 0 54 54" fill="none" stroke="var(--sky)" stroke-width="2.5"><rect x="8" y="4" width="38" height="46"/><line x1="8" y1="18" x2="46" y2="18"/><line x1="8" y1="33" x2="46" y2="33"/><rect x="13" y="8" width="7" height="10"/><rect x="23" y="10" width="6" height="8"/><rect x="32" y="23" width="8" height="10"/><rect x="14" y="38" width="9" height="12"/><rect x="28" y="41" width="7" height="9"/></svg>
      <div class="service-name">PANTRY SERVICE</div>
    </div>
    <div class="service">
      <svg viewBox="0 0 54 54" fill="none" stroke="var(--sky)" stroke-width="2.5"><path d="M6 6h42l4 12H2z"/><path d="M2 18c0 4 5 6 8 2 3 4 8 4 10 0 3 4 8 4 10 0 3 4 8 4 10 0 3 4 8 2 12-2"/><line x1="7" y1="24" x2="7" y2="50"/><line x1="47" y1="24" x2="47" y2="50"/><line x1="4" y1="50" x2="50" y2="50"/><rect x="13" y="32" width="12" height="18"/><rect x="30" y="32" width="11" height="9"/></svg>
      <div class="service-name">MICRO-MARKET</div>
    </div>
  </div>

  <ul class="values">
    <li><svg viewBox="0 0 16 16"><path d="M2 8.5l4 4 8-9" fill="none" stroke="var(--sky)" stroke-width="2.6"/></svg>We are obsessed with Customer Service</li>
    <li><svg viewBox="0 0 16 16"><path d="M2 8.5l4 4 8-9" fill="none" stroke="var(--sky)" stroke-width="2.6"/></svg>We strive for Innovation &amp; Variety</li>
    <li><svg viewBox="0 0 16 16"><path d="M2 8.5l4 4 8-9" fill="none" stroke="var(--sky)" stroke-width="2.6"/></svg>We are highly focused on Reliability &amp; Maintenance</li>
    <li><svg viewBox="0 0 16 16"><path d="M2 8.5l4 4 8-9" fill="none" stroke="var(--sky)" stroke-width="2.6"/></svg>We care for our Community &amp; Environment</li>
    <li><svg viewBox="0 0 16 16"><path d="M2 8.5l4 4 8-9" fill="none" stroke="var(--sky)" stroke-width="2.6"/></svg>Quality Assurance is non-negotiable</li>
    <li><svg viewBox="0 0 16 16"><path d="M2 8.5l4 4 8-9" fill="none" stroke="var(--sky)" stroke-width="2.6"/></svg>We seek to continuously Learn &amp; Improve</li>
    <li><svg viewBox="0 0 16 16"><path d="M2 8.5l4 4 8-9" fill="none" stroke="var(--sky)" stroke-width="2.6"/></svg>Safety and Hygiene are paramount</li>
    <li><svg viewBox="0 0 16 16"><path d="M2 8.5l4 4 8-9" fill="none" stroke="var(--sky)" stroke-width="2.6"/></svg>We are Good People with Uncompromising Integrity</li>
  </ul>

  <div class="footer">
    <svg class="footer-web" width="400" height="64" viewBox="0 0 400 64" aria-hidden="true">
      <polygon points="0,0 400,0 365,64 0,64" fill="var(--white)"/>
      <polygon points="0,0 388,0 353,64 0,64" fill="var(--navy-deep)"/>
    </svg>
    <div class="footer-web-text">steadypointvend.com</div>
    <div class="footer-address">1480 Maple Ridge Rd. Suite 210, Westbrook, Illinois 60599, US</div>
  </div>
</div>
</body>
</html>
```